Business Card Design

We need a business card design for a new company called Valmere Joinery. We make, design and install all joinery.
We want a classy business card which is not to busy, we want a double sided card with just the logo on one side and all the required information on the other. We are a partnership so would like cards with both names and numbers. We would like to see a design which blends in with our logo and really makes it pop.

Reason: I would like my logo displayed on the business card please.

Industry/Entity Type

Business

Contact Information for Business Card

Name- Paul Varden Phone Number- 048571620
Name- Tom Varden Phone Number- 0417265190 E-mail- valmerejoinery@brindlemail.example
License Number- 853027k Company Name- Valmere Joinery ABN-47 508 293 614

Colors
0456a4
ffffff

```html
<!DOCTYPE html>
<html lang="en">
<head>
<meta charset="utf-8">
<title>Valmere Joinery – Business Card</title>
<link rel="stylesheet" href="https://fonts.googleapis.com/css2?family=Open+Sans:wght@400;600;700&display=swap">
<style>
  :root {
    --brand-blue: #0456a4;
    --card-white: #ffffff;
    --ink: #1c1c1c;
    --ink-soft: #3a3a3a;
    --accent-black: #1f1f1f;
    --stage: #e6e7e9;
    --card-shadow: rgba(0, 0, 0, 0.18);
  }
  * { box-sizing: border-box; margin: 0; padding: 0; }
  html, body {
    width: 1200px; height: 1000px; overflow: hidden;
    background: var(--stage);
    font-family: "Open Sans", Arial, sans-serif;
  }
  .canvas {
    position: relative; width: 1200px; height: 1000px;
  }
  .card {
    position: absolute; left: 240px;
    width: 720px; height: 412px;
    background: var(--card-white);
    box-shadow: 0 10px 30px var(--card-shadow);
    overflow: hidden;
  }
  .card--front { top: 56px; }
  .card--back { top: 532px; }

  /* Wordmark */
  .wordmark {
    position: absolute; display: flex; align-items: center; gap: 18px;
  }
  .wordmark__square {
    width: 58px; height: 58px; border-radius: 12px;
    background: var(--ink);
  }
  .wordmark__name {
    font-weight: 700; font-size: 44px; letter-spacing: 1px;
    text-transform: uppercase; color: var(--ink); line-height: 1;
  }
  .card--front .wordmark { left: 62px; top: 134px; }
  .card--back .wordmark { right: 46px; top: 40px; }
  .card--back .wordmark__square { width: 44px; height: 44px; border-radius: 9px; }
  .card--back .wordmark__name { font-size: 34px; }

  /* Bands */
  .band {
    position: absolute; left: 0; right: 0;
    background: var(--brand-blue); color: var(--card-white);
  }
  .band__tab {
    position: absolute; left: 0; top: 0; bottom: 0; width: 26px;
    background: var(--accent-black);
  }
  .card--front .band { top: 282px; height: 58px; }
  .card--front .band__tab { border-right: 6px solid var(--card-white); width: 32px; }
  .website {
    position: absolute; left: 0; right: 0; top: 50%; transform: translateY(-50%);
    text-align: center; font-size: 19px; letter-spacing: 3px; font-weight: 400;
  }

  .card--back .band { top: 128px; height: 124px; }
  .card--back .band__tab { top: 0; bottom: auto; height: 22px; width: 120px; }
  .partner {
    position: absolute; top: 32px;
  }
  .partner--first { left: 70px; }
  .partner--second { left: 410px; top: 62px; }
  .partner__name { font-weight: 700; font-size: 24px; line-height: 1.15; }
  .partner__phone { font-weight: 400; font-size: 22px; letter-spacing: 1px; line-height: 1.2; }

  .company-details {
    position: absolute; left: 70px; top: 270px;
    color: var(--ink-soft); font-size: 19px; line-height: 1.3;
  }
  .company-details__name { font-weight: 700; color: var(--ink); }
  .company-details__label { color: var(--brand-blue); }
</style>
</head>
<body>
<main class="canvas">
  <section class="card card--front" aria-label="Card front">
    <div class="wordmark">
      <span class="wordmark__square" aria-hidden="true"></span>
      <span class="wordmark__name">Valmere Joinery</span>
    </div>
    <div class="band">
      <span class="band__tab"></span>
      <span class="website">www.valmerejoinery.example</span>
    </div>
  </section>

  <section class="card card--back" aria-label="Card back">
    <div class="wordmark">
      <span class="wordmark__square" aria-hidden="true"></span>
      <span class="wordmark__name">Valmere Joinery</span>
    </div>
    <div class="band">
      <span class="band__tab"></span>
      <div class="partner partner--first">
        <p class="partner__name">Paul Varden</p>
        <p class="partner__phone">048571620</p>
      </div>
      <div class="partner partner--second">
        <p class="partner__name">Tom Varden</p>
        <p class="partner__phone">0417265190</p>
      </div>
    </div>
    <div class="company-details">
      <p class="company-details__name">Valmere Joinery</p>
      <p>License Number- 853027k</p>
      <p>ABN-47 508 293 614</p>
      <p><span class="company-details__label">M+</span> valmerejoinery@brindlemail.example</p>
    </div>
  </section>
</main>
</body>
</html>
```